Quill Pet Shop Homepage

We are a pet shop, we focus on dog food / cat food / rodents & bird food

Based on WooCommerce

It should be a simple but professional homepage with an informative start page. In the shop it should then be possible to shop for products/manufacturers etc. Navigation/Filter menu on the left would be ideal.

Next menus:
ABOUT US
CONTACT
DOG
CAT
HOLDER

My Account - Login
My Cart

Footer:
Conditions
payment options
social media

In addition to our logo, I have attached 2 example pages from another shop which we would use as a guideline.

Target Market(s)

pet store

Industry/Entity Type

Animal, Pet Shop

Coding

Coded - Design and coding required

Number of Pages Required

1 page

Font styles to use
Sans Serif

Colors
0054AA
0677BA
7BADD7
CADEEF
E8F1F8

Requirements
Must have
• Main Page, Contact, About Us, Shop, Check Out, Member Login, Mailchimp Marketing - We work with WooCommerce

```html
<!DOCTYPE html>
<html lang="en">
<head>
<meta charset="utf-8">
<title>Quill Pet Shop – Premium Pet Food</title>
<link href="https://fonts.googleapis.com/css2?family=Lato:wght@400;700;900&display=swap" rel="stylesheet">
<style>
:root{
  --blue:#0054AA;
  --blue-2:#0677BA;
  --blue-3:#7BADD7;
  --blue-4:#CADEEF;
  --blue-5:#E8F1F8;
  --ink:#111;
  --text:#444;
  --grey-bg:#F2F2F2;
  --card-grey:#EFEFEF;
  --footer:#1E1E1E;
  --star:#F4B400;
}
*{box-sizing:border-box;margin:0;padding:0}
html,body{width:1200px;height:3382px;overflow:hidden}
body{font-family:'Lato',sans-serif;color:var(--text);background:#fff;position:relative}
.abs{position:absolute}
a{color:inherit;text-decoration:none}

/* header */
.brand{left:112px;top:14px;display:flex;align-items:center;gap:10px;font-weight:900;font-size:26px;color:var(--blue);letter-spacing:1px}
.brand .dot{width:40px;height:40px;border-radius:50%;background:var(--blue)}
.topbar{top:14px;left:446px;display:flex;align-items:center;font-size:15px;font-weight:700;color:#222}
.topbar .ic{width:32px;height:32px;border-radius:50%;border:2px solid var(--blue-4);display:flex;align-items:center;justify-content:center;margin-right:12px}
.topbar .sep{width:1px;height:18px;background:#333;margin:0 28px}
.login{background:var(--blue);color:#fff;border-radius:20px;padding:6px 16px;display:flex;align-items:center;gap:8px;font-size:17px}
.navbar{top:59px;left:378px;width:822px;height:46px;background:var(--blue);clip-path:polygon(38px 0,100% 0,100% 100%,0 100%)}
.nav{top:59px;left:432px;height:46px;display:flex;align-items:center;color:#fff;font-size:14px;font-weight:700}
.nav a{margin-right:60px}
.nav a.active{text-decoration:underline;text-underline-offset:4px}
.headline{top:103px;left:0;width:1200px;height:3px;background:var(--blue)}

/* hero */
.hero-photo{top:105px;left:0;width:1200px;height:660px;background:linear-gradient(100deg,#f4f4f4 0%,#e8e6e3 35%,#9a9a9c 50%,#c78a4a 70%,#d9a15e 85%,#eee 100%)}
.hero-text{top:214px;left:110px;color:#111}
.hero-text .k1{font-size:28px;font-weight:700;letter-spacing:7px}
.hero-text h1{font-size:74px;font-weight:900;letter-spacing:2px;line-height:1;margin-top:14px}
.hero-text .k2{font-size:19px;font-weight:700;letter-spacing:5px;margin-top:22px}
.hero-text p{font-size:15px;line-height:31px;width:400px;margin-top:14px;color:#333}
.btn{display:inline-block;background:var(--blue);color:#fff;font-weight:900;border-radius:30px;text-align:center}
.hero-btn{top:491px;left:111px;width:171px;height:54px;line-height:54px;font-size:17px}

/* section headings */
.sec-title{left:0;width:1200px;display:flex;justify-content:center;align-items:center;gap:16px;font-size:37px;font-weight:900;color:#111}
.sec-title .dot{width:52px;height:52px;border-radius:50%;background:var(--blue);border:3px solid var(--blue-4)}
.sec-title span{color:var(--blue)}

/* products */
.card{top:888px;width:284px;height:404px;overflow:hidden;text-align:center}
.card.light{background:var(--blue-4)}
.card.grey{background:var(--card-grey)}
.card h3{font-size:24px;font-weight:900;color:var(--blue);margin-top:27px}
.card p{font-size:12.5px;font-weight:700;color:#222;line-height:23px;margin:12px 22px 0}
.card a{display:block;margin-top:12px;font-size:14px;font-weight:900;color:var(--blue);text-decoration:underline}
.card .photo{position:absolute;left:0;bottom:0;width:100%;height:200px}

/* about */
.about-bg{top:1376px;left:0;width:1200px;height:483px;background:var(--grey-bg)}
.about-art{top:1428px;left:118px;width:375px;height:375px;border-radius:50%;background:var(--blue);box-shadow:8px 6px 0 #c9c9c9}
.about-title{top:1431px;left:552px;display:flex;align-items:center;gap:14px;font-size:37px;font-weight:900;color:#111}
.about-title .dot{width:52px;height:52px;border-radius:50%;background:var(--blue);border:3px solid var(--blue-4)}
.about-title span{color:var(--blue)}
.about-copy{top:1494px;left:552px;width:545px;font-size:15px;line-height:29px;color:#444}
.about-copy p+p{margin-top:29px}
.about-btn{top:1737px;left:554px;width:171px;height:53px;line-height:53px;font-size:17px}

/* testimonials */
.tcard{width:306px;background:#fff;border:1px solid #ddd;padding:26px 16px 0}
.tcard.mid{border:none;background:#FAFAFA;box-shadow:0 3px 12px rgba(0,0,0,.08)}
.stars{color:var(--star);font-size:19px;letter-spacing:1px}
.tcard p{font-size:15px;line-height:27px;color:#333;margin-top:14px}
.person{display:flex;align-items:center;gap:12px;margin-top:20px}
.avatar{width:62px;height:62px;border-radius:50%;background:linear-gradient(135deg,#c9b8a6,#6f5d4f);border:2px solid var(--blue-4)}
.person b{display:block;font-size:14px;color:#111}
.person small{font-size:12px;color:#999;font-weight:700}

/* newsletter */
.news{top:2454px;left:0;width:1200px;height:353px;background:linear-gradient(180deg,#0a5aa8 0%,#0b4f92 60%,#0d4582 100%)}
.news h2{position:absolute;top:60px;width:100%;text-align:center;color:#fff;font-size:37px;font-weight:900;letter-spacing:1px}
.news p{position:absolute;top:120px;left:160px;width:880px;text-align:center;color:#fff;font-size:15px;font-weight:700;line-height:29px}
.news .field{position:absolute;top:219px;left:223px;width:751px;height:62px;background:#fff;border-radius:31px;display:flex;align-items:center;justify-content:space-between;padding:0 6px 0 28px;font-size:13px;color:#777}
.news .sub{background:#d3d3d3;color:#222;font-weight:900;font-size:18px;border-radius:26px;width:160px;height:50px;line-height:50px;text-align:center;letter-spacing:1px}

/* footer */
.footer{top:2807px;left:0;width:1200px;height:575px;background:var(--footer);color:#fff}
.fnav{position:absolute;top:74px;left:265px;display:flex;font-size:15px;font-weight:900}
.fnav a{margin-right:68px}
.rule{position:absolute;left:112px;width:977px;height:1px;background:#666}
.flogo{position:absolute;top:189px;left:112px;width:220px;height:86px;background:#fff;display:flex;align-items:center;justify-content:center;gap:10px;color:var(--blue);font-weight:900;font-size:20px;letter-spacing:1px}
.flogo .dot{width:32px;height:32px;border-radius:50%;background:var(--blue)}
.fcontact{position:absolute;top:292px;left:112px;font-size:14px;line-height:24px}
.fcontact div{display:flex;gap:12px;margin-bottom:10px;align-items:flex-start}
.social{position:absolute;top:424px;left:112px;display:flex;gap:14px}
.social i{width:25px;height:25px;border-radius:50%;background:#fff;display:block;border:3px solid var(--blue-3)}
.fh{position:absolute;font-size:21px;font-weight:900;letter-spacing:.5px}
.form{position:absolute;top:235px;left:394px;width:445px}
.form .in{background:#fff;color:#666;font-size:10px;padding:0 12px;height:40px;line-height:40px}
.form .row{display:flex;gap:8px;margin-bottom:8px}
.form .row .in{flex:1}
.form .msg{height:72px;line-height:26px;margin-bottom:18px}
.form .send{display:inline-block;background:var(--blue);border-radius:18px;font-size:12px;font-weight:900;padding:0 22px;height:34px;line-height:34px}
.help{position:absolute;top:237px;left:903px;font-size:15px;line-height:43px}
.copy{position:absolute;top:530px;left:112px;font-size:15px}
.pay{position:absolute;top:532px;left:886px;display:flex;gap:6px}
.pay i{display:block;width:28px;height:18px;border-radius:3px;background:#fff}
</style>
</head>
<body>

<div class="abs brand"><span class="dot"></span>QUILL PET</div>
<div class="abs topbar">
  <span class="ic"><svg width="14" height="14" viewBox="0 0 24 24"><path fill="#0054AA" d="M6.6 10.8a15 15 0 0 0 6.6 6.6l2.2-2.2c.3-.3.7-.4 1-.2 1.1.4 2.3.6 3.6.6.6 0 1 .4 1 1V20c0 .6-.4 1-1 1A17 17 0 0 1 3 4c0-.6.4-1 1-1h3.5c.6 0 1 .4 1 1 0 1.3.2 2.5.6 3.6.1.3 0 .7-.2 1z"/></svg></span>
  +1 555 014 2290
  <span class="sep"></span>
  <span class="ic"><svg width="14" height="12" viewBox="0 0 24 18"><path fill="#0054AA" d="M0 0h24v18H0z"/><path d="M0 0l12 10L24 0" stroke="#fff" stroke-width="2" fill="none"/></svg></span>
  info@quillpet.com
  <span class="sep"></span>
  <span class="login"><svg width="18" height="18" viewBox="0 0 24 24" fill="none" stroke="#fff" stroke-width="2"><circle cx="12" cy="12" r="10"/><path d="M7 12h9M12 8l4 4-4 4"/></svg>Login</span>
  <span class="sep"></span>
  <svg width="26" height="24" viewBox="0 0 26 24"><path d="M1 2h4l3 13h12l3-9H7" fill="none" stroke="#111" stroke-width="2.5"/><circle cx="10" cy="20" r="2" fill="#111"/><circle cx="19" cy="20" r="2" fill="#111"/><circle cx="22" cy="3" r="5" fill="#0054AA"/><text x="22" y="6" font-size="7" fill="#fff" text-anchor="middle" font-family="Lato">2</text></svg>
</div>
<div class="abs navbar"></div>
<nav class="abs nav">
  <a class="active">HOME</a><a>ABOUT US</a><a>CONTACT</a><a>DOG</a><a>CAT</a><a>HOLDER</a>
  <svg width="14" height="14" viewBox="0 0 24 24" fill="none" stroke="#fff" stroke-width="2.5"><circle cx="10" cy="10" r="7"/><path d="M15 15l7 7"/></svg>
</nav>
<div class="abs headline"></div>

<div class="abs hero-photo" role="img" aria-label="Photo of a grey cat and a golden retriever cuddling on a bright floor"></div>
<svg class="abs" style="top:600px;left:0" width="1200" height="170" viewBox="0 0 1200 170">
  <path d="M0 20 Q600 255 1200 20 V170 H0Z" fill="#fff"/>
  <path d="M0 20 Q600 255 1200 20 L1200 28 Q600 275 0 32Z" fill="#0054AA"/>
</svg>
<svg class="abs" style="top:673px;left:570px" width="60" height="20"><circle cx="7" cy="10" r="3.5" fill="#666"/><circle cx="30" cy="10" r="8" fill="none" stroke="#0054AA" stroke-width="2"/><circle cx="30" cy="10" r="4.5" fill="#0054AA"/><circle cx="53" cy="10" r="3.5" fill="#666"/></svg>
<div class="abs hero-text">
  <div class="k1">WELCOME TO</div>
  <h1>QUILL PET</h1>
  <div class="k2">PREMIUM PET FOOD</div>
  <p>Itaque earum rerum hic tenetur a sapiente delectus, ut aut reiciendis voluptatibus maiores alias consequatur asperiores repellat.</p>
</div>
<a class="abs btn hero-btn">GET STARTED</a>

<div class="abs sec-title" style="top:808px"><i class="dot"></i>OUR <span>PRODUCTS</span></div>

<div class="abs card light" style="left:11px">
  <h3>DOG FOOD</h3>
  <p>Temporibus autem quibusdam et aut officiis debitis aut rerum necessitatibus saepe eveniet ut et voluptates repudiandae sirecusandae.</p>
  <a>VIEW MORE</a>
  <div class="photo" role="img" aria-label="Golden retriever beside a bowl of dry dog food" style="background:linear-gradient(90deg,#d6a46a,#e9c79a 55%,#CADEEF)"></div>
</div>
<div class="abs card grey" style="left:310px">
  <h3>CAT FOOD</h3>
  <p>Nam libero tempore, cum soluta nobis est eligendi optio cumque nihil impedit quo minus id quod maxime placeat facere possimus.</p>
  <a>VIEW MORE</a>
  <div class="photo" role="img" aria-label="Tabby kitten next to a bowl of cat food" style="background:linear-gradient(90deg,#EFEFEF,#a3958a 45%,#c9a46a 60%,#EFEFEF)"></div>
</div>
<div class="abs card light" style="left:607px">
  <h3>RODENTS FOOD</h3>
  <p>Itaque earum rerum hic tenetur a sapiente delectus, ut aut reiciendis voluptatibus maiores alias consequatur aut perferendis doloribus asperiores</p>
  <a>VIEW MORE</a>
  <div class="photo" role="img" aria-label="Hamster eating seeds and greens" style="background:linear-gradient(90deg,#CADEEF,#e8a66a 40%,#f0c79a 65%,#CADEEF)"></div>
</div>
<div class="abs card grey" style="left:905px">
  <h3>BIRD FOOD</h3>
  <p>Nam libero tempore, cum soluta nobis est eligendi optio cumque nihil impedit quo minus id quod maxime placeat facere possimus.</p>
  <a>VIEW MORE</a>
  <div class="photo" role="img" aria-label="Sparrow and blue tit on a pile of bird seed" style="background:linear-gradient(90deg,#EFEFEF,#8a7a66 35%,#b9a27a 60%,#c8c45a 80%,#EFEFEF)"></div>
</div>

<div class="abs about-bg"></div>
<div class="abs about-art" role="img" aria-label="Brand illustration of a dog, cat, rabbit and birds"></div>
<div class="abs about-title"><i class="dot"></i>ABOUT <span>QUILL PET</span></div>
<div class="abs about-copy">
  <p>Nam libero tempore, cum soluta nobis est eligendi optio cumque nihil impedit quo mi voluptas assumenda est, omnis dolor repellendus. Temporibus autem quibusdam et aut officiis debitis aut rerum necessitatibus saepe eveniet ut et voluptates repudiandae sint et molestiae non recusandae.</p>
  <p>Itaque earum rerum hic tenetur a sapiente delectus, ut aut reiciendis delectus, ut aut reiciendis voluptatibus maiores alias consequatur aut perferendis doloribus asperiores repellat.</p>
</div>
<a class="abs btn about-btn">READ MORE</a>

<div class="abs sec-title" style="top:1915px"><i class="dot"></i>WHAT <span>CUSTOMER SAYS</span></div>

<div class="abs tcard" style="top:2001px;left:109px;height:336px">
  <div class="stars">★★★★★</div>
  <p>Temporibus autem quibusdam et aut officiis debitis aut rerum neus saepe facere mus, onis volupta seveniet ut et voluptates repudae sint et facere mus, onis volupta seveniet ut et molestiae non lorem recusadae.</p>
  <div class="person"><i class="avatar"></i><div><b>Owen Barlow</b><small>United States</small></div></div>
</div>
<div class="abs tcard mid" style="top:2039px;left:446px;height:335px">
  <div class="stars">★★★★★</div>
  <p>Itaque earum rerum hic tenetur a sapiene delectus, ut aut reicieis voibus maiores alias confacere mus, onis volupta seveniet ut et se uatur aut perferndis doloribus asiores reiciendis voluptatbus repalat</p>
  <div class="person"><i class="avatar"></i><div><b>Lena</b><small>United States</small></div></div>
</div>
<div class="abs tcard" style="top:2002px;left:783px;height:336px">
  <div class="stars">★★★★★</div>
  <p>At vero eos et accusamus et iusto odio dignissimos ducfacere mus, onis volupta seveniet ut et imus qui blaiis praesentium voluptum deleniti atque corrupti quos dolores et quas occaati cupie non provident</p>
  <div class="person"><i class="avatar"></i><div><b>Marcus Hale</b><small>United States</small></div></div>
</div>

<section class="abs news">
  <h2>JOIN OUR NEWSLETTER</h2>
  <p>Temporibus autem quibusdam et aut officiis debitis aut rerum necessitatibus saepe eveniet ut et voluptates repudiandae sint et molestiae non recusandae. Itaque earum rerum hic tenetur a sapiente delectus, ut aut reiciendis voluptatibus maiores alias consequatur aut perferendis doloribus asperiores repellat.</p>
  <div class="field">Enter The Email<span class="sub">SUBSCRIBE</span></div>
</section>

<footer class="abs footer">
  <div class="fnav"><a>HOME</a><a>ABOUT US</a><a>PETS</a><a>PREMIUM PET FOOD</a><a>CONTACT US</a></div>
  <div class="rule" style="top:137px"></div>

  <div class="flogo"><i class="dot"></i>QUILL PET</div>
  <div class="fcontact">
    <div><svg width="16" height="16" viewBox="0 0 24 24"><path fill="#fff" d="M6.6 10.8a15 15 0 0 0 6.6 6.6l2.2-2.2c.3-.3.7-.4 1-.2 1.1.4 2.3.6 3.6.6.6 0 1 .4 1 1V20c0 .6-.4 1-1 1A17 17 0 0 1 3 4c0-.6.4-1 1-1h3.5c.6 0 1 .4 1 1 0 1.3.2 2.5.6 3.6.1.3 0 .7-.2 1z"/></svg>+1 555 014 2290</div>
    <div><svg width="14" height="20" viewBox="0 0 14 20"><path fill="#fff" d="M7 0a7 7 0 0 0-7 7c0 5 7 13 7 13s7-8 7-13a7 7 0 0 0-7-7zm0 9.5a2.5 2.5 0 1 1 0-5 2.5 2.5 0 0 1 0 5z"/></svg><span>Quill Pet, Premium Pet Food<br>United States</span></div>
    <div><svg width="16" height="12" viewBox="0 0 24 18"><path fill="#fff" d="M0 0h24v18H0z"/><path d="M0 0l12 10L24 0" stroke="#1E1E1E" stroke-width="2" fill="none"/></svg>info@quillpet.com</div>
  </div>
  <div class="social"><i></i><i></i><i></i><i></i></div>

  <div class="fh" style="top:188px;left:394px">GET IN TOUCH</div>
  <div class="form">
    <div class="row"><div class="in">Name</div><div class="in">Phone No</div></div>
    <div class="row"><div class="in">Email</div></div>
    <div class="in msg">Msg</div>
    <span class="send">SUBMIT</span>
  </div>

  <div class="fh" style="top:188px;left:903px">HELP LINKS</div>
  <div class="help">
    <div>›&nbsp; FAQ</div><div>›&nbsp; Terms of Use</div><div>›&nbsp; Privacy Policy</div><div>›&nbsp; Conditions</div><div>›&nbsp; Support Center</div>
  </div>

  <div class="rule" style="top:495px"></div>
  <div class="copy">Copyrights@2023.Quill Pet.All Rights Reserved</div>
  <div class="pay" aria-label="Accepted payment methods"><i></i><i></i><i></i><i></i><i></i><i></i></div>
</footer>

</body>
</html>
```